Design a web site for my business - Finish Craft Coralbay.

We are a family business that handles design, fabrication and installation of powder coated aluminum, stainless steel and glass products. Including handrails, privacy slat screens, electric gates and pool fencing. We are based in the Whitsundays in North Queensland and service an area from Airlie Beach to Townsville.

Target Market(s)

Domestic and commercial

Industry/Entity Type

fabrication - manufacturing

Coding

Coded - Design and coding required

Number of Pages Required

5+ page

Colors
0054AA
0677BA
7BADD7
CADEEF
E8F1F8

Requirements
Must have
• photo galleries, contact page, one page for privacy screens, balustrades, glass fencing, stainless steel handrail, powder coated aluminium handrails and pool fencing

```html
<!DOCTYPE html>
<html lang="en">
<head>
<meta charset="utf-8">
<title>Finish Craft Coralbay</title>
<link href="https://fonts.googleapis.com/css2?family=Poppins:wght@400;500;600;700&family=Oswald:wght@400;500&family=Inter:wght@400;500;600;700&display=swap" rel="stylesheet">
<style>
:root{
  --navy:#0b1a3a;
  --navy-deep:#09152f;
  --teal:#1aa3aa;
  --brand:#0054AA;
  --brand-mid:#0677BA;
  --brand-soft:#7BADD7;
  --brand-pale:#CADEEF;
  --brand-mist:#E8F1F8;
  --accent:#f25a38;
  --ink:#111;
  --muted:#555;
  --band:#f2f2f2;
  --pin:#ef2d3a;
}
*{margin:0;padding:0;box-sizing:border-box}
html,body{width:1200px;height:3358px;overflow:hidden}
body{position:relative;font-family:"Poppins",sans-serif;color:var(--ink);background:#fff}
.abs{position:absolute}
/* header */
.header{left:0;top:0;width:1200px;height:133px;background:var(--navy)}
.brand{left:117px;top:45px;display:flex;align-items:center;gap:10px;color:#fff}
.brand-mark{width:42px;height:42px;border:3px solid #fff;border-radius:50%}
.brand-name{font-weight:600;font-size:15px;line-height:18px;width:110px}
.nav{left:309px;top:56px;display:flex;gap:45px;font-size:15px;font-weight:500;color:#fff}
.phone-btn{left:926px;top:40px;width:156px;height:51px;border:2px solid var(--teal);border-radius:4px;color:#fff;display:flex;align-items:center;justify-content:center;gap:10px;font-size:15px;font-weight:500}
/* hero */
.hero{left:0;top:133px;width:1200px;height:604px;background:linear-gradient(90deg,#1e3a5c 0%,#2f5572 40%,#8c9ea8 70%,#b9c4c6 100%)}
.hero-title{left:117px;top:318px;width:660px;font-size:51px;font-weight:600;line-height:70px;color:#fff}
.hero-sub{left:117px;top:472px;width:630px;font-size:13.5px;line-height:22px;color:#dfe6ec}
.btn-quote{left:117px;top:593px;width:243px;height:63px;background:var(--teal);color:#fff;font-size:14px;font-weight:600;display:flex;align-items:center;justify-content:center}
/* stats */
.stats{left:0;top:737px;width:1200px;height:111px;background:var(--band)}
.stat{top:768px;display:flex;align-items:center;gap:12px}
.stat-num{font-family:"Oswald",sans-serif;font-size:44px;color:var(--accent);line-height:1}
.stat-label{font-family:"Inter",sans-serif;font-size:14px;line-height:22px;letter-spacing:1.5px;color:#555}
/* about */
.about-shadow{left:127px;top:941px;width:497px;height:456px;background:#f8c3c0;border-radius:14px}
.about-img{left:117px;top:931px;width:499px;height:458px;border-radius:14px;background:linear-gradient(180deg,#b7704f 0%,#d9cfc3 22%,#ece7df 60%,#c9bda9 86%,#5aa3b6 100%)}
.about-bar{left:682px;top:949px;width:5px;height:30px;background:var(--brand)}
.about-title{left:700px;top:938px;font-size:36px;font-weight:700}
.about-text{left:700px;top:1010px;width:380px;font-size:14px;line-height:29.2px;color:#444}
.btn-more{left:702px;top:1335px;width:185px;height:70px;background:var(--brand);color:#fff;font-family:"Inter",sans-serif;font-size:15px;font-weight:600;letter-spacing:1.5px;display:flex;align-items:center;justify-content:center}
/* products */
.section-title{font-family:"Inter",sans-serif;font-weight:700;font-size:26px}
.view-all{left:1020px;top:1524px;width:62px;text-align:right;font-family:"Inter",sans-serif;font-size:14px;color:#888}
.card{top:1571px;width:264px;height:506px;background:#fff;border-radius:6px;box-shadow:0 3px 14px rgba(0,0,0,.08)}
.card-img{position:absolute;left:20px;top:19px;width:224px;height:227px;border-radius:6px}
.badge{position:absolute;left:27px;top:25px;background:#2d8f5c;color:#fff;font-family:"Inter",sans-serif;font-size:12px;font-weight:600;padding:3px 10px;border-radius:3px}
.card-title{position:absolute;left:20px;top:266px;width:230px;font-family:"Inter",sans-serif;font-weight:700;font-size:14.5px;line-height:25px;letter-spacing:.3px}
.card-org{position:absolute;left:20px;top:331px;font-family:"Inter",sans-serif;font-size:11.5px;color:#555;text-transform:uppercase}
.card-meta{position:absolute;left:20px;top:373px;font-family:"Inter",sans-serif;font-size:11.5px;color:#444;line-height:26px}
.card-meta div{display:flex;align-items:center;gap:10px;text-transform:uppercase}
.dot{width:14px;height:14px;border-radius:50%;background:#f28b76;display:inline-block}
.btn-cart{position:absolute;left:20px;top:437px;width:224px;height:52px;border:1.5px solid var(--brand);border-radius:2px;color:var(--brand);font-family:"Inter",sans-serif;font-size:13px;font-weight:600;display:flex;align-items:center;justify-content:center}
/* services map */
.map{left:248px;top:2217px;width:727px;height:495px;background:radial-gradient(ellipse at 50% 45%,#c4c4c4 0%,#d0d0d0 45%,#fff 75%)}
.pin{position:absolute;width:46px;height:58px}
/* cta */
.cta{left:0;top:2767px;width:1200px;height:274px;background:linear-gradient(180deg,#3c4446 0%,#2a3234 55%,#1b2224 100%)}
.cta-title{left:0;top:2845px;width:1200px;text-align:center;font-family:"Inter",sans-serif;font-size:25px;font-weight:600;color:#fff}
.cta-sub{left:250px;top:2891px;width:700px;text-align:center;font-family:"Inter",sans-serif;font-size:10.5px;line-height:17px;color:#e9e9e9;text-transform:uppercase}
/* footer */
.footer{left:0;top:3041px;width:1200px;height:266px;background:var(--navy)}
.footer-bottom{left:0;top:3307px;width:1200px;height:51px;background:var(--navy-deep);color:#7c879c;font-family:"Inter",sans-serif;font-size:10px;text-align:center;line-height:51px}
.f-brand{left:163px;top:3103px}
.f-about{left:163px;top:3188px;width:220px;font-family:"Inter",sans-serif;font-size:10px;line-height:12px;color:#e2e6ee}
.f-social{left:163px;top:3269px;display:flex;gap:11px}
.f-social span{width:18px;height:18px;border-radius:50%;background:#fff}
.f-col{top:3104px;font-family:"Inter",sans-serif;color:#fff}
.f-col h4{font-size:12px;font-weight:500;margin-bottom:17px}
.f-col li{list-style:none;font-size:10px;line-height:22px;color:#dfe3ea;display:flex;align-items:center;gap:8px}
.ico{width:11px;height:11px;border-radius:2px;background:var(--accent);display:inline-block}
</style>
</head>
<body>

<header class="abs header"></header>
<div class="abs brand"><span class="brand-mark"></span><span class="brand-name">Finish Craft Coralbay</span></div>
<nav class="abs nav"><span>Home</span><span>About Us</span><span>Products</span><span>Projects</span><span>Services</span><span>Gallery</span></nav>
<div class="abs phone-btn">
  <svg width="15" height="15" viewBox="0 0 24 24"><path fill="#fff" d="M6.6 10.8a15.1 15.1 0 0 0 6.6 6.6l2.2-2.2c.3-.3.7-.4 1-.2 1.1.4 2.3.6 3.6.6.6 0 1 .4 1 1V20c0 .6-.4 1-1 1C10.6 21 3 13.4 3 4c0-.6.4-1 1-1h3.5c.6 0 1 .4 1 1 0 1.3.2 2.5.6 3.6.1.3 0 .7-.2 1z"/></svg>
  4000-555-100
</div>

<section class="abs hero" role="img" aria-label="Modern white home with glass balustrades, terrace and blue pool"></section>
<h1 class="abs hero-title">Built to Last. Designed for Queensland Living.</h1>
<p class="abs hero-sub">Premium aluminium, stainless steel and glass fabrication for homes and businesses across the Whitsundays, Airlie Beach, Bowen and Townsville.</p>
<div class="abs btn-quote">GET A FREE QUOTE</div>

<section class="abs stats"></section>
<div class="abs stat" style="left:157px"><span class="stat-num">18+</span><span class="stat-label">Excelence<br>Awards</span></div>
<div class="abs stat" style="left:402px"><span class="stat-num">485+</span><span class="stat-label">Happy<br>Clients</span></div>
<div class="abs stat" style="left:650px"><span class="stat-num">12+</span><span class="stat-label">Worldwide<br>Connection</span></div>
<div class="abs stat" style="left:883px"><span class="stat-num">287+</span><span class="stat-label">Number of<br>Resorts</span></div>

<div class="abs about-shadow"></div>
<div class="abs about-img" role="img" aria-label="White rendered house with terracotta roof, stone wall and poolside paving"></div>
<div class="abs about-bar"></div>
<h2 class="abs about-title">Locals Who Care</h2>
<p class="abs about-text">Finish Craft Coralbay is a family business based in the Whitsundays, designing and building quality products for homes and businesses.<br>We handle every step in-house, from design and fabrication to installation of powder coated aluminium, stainless steel and glass, including handrails, privacy slat screens, electric gates, balustrades and pool fencing, servicing the coast from Airlie Beach to Townsville.</p>
<div class="abs btn-more">MORE ABOUT US</div>

<h2 class="abs section-title" style="left:117px;top:1515px">OUR PRODUCTS</h2>
<div class="abs view-all">View All</div>

<article class="abs card" style="left:117px">
  <div class="card-img" role="img" aria-label="Resort pavilion beside a long turquoise pool" style="background:linear-gradient(180deg,#9fc0d6 0%,#4e4a3d 45%,#2f8f8c 100%)"></div>
  <span class="badge">NEW</span>
  <h3 class="card-title">ALUMINIUM POOL FENCING PANELS</h3>
  <div class="card-org">Powder coated aluminium</div>
  <div class="card-meta"><div><span class="dot"></span>Airlie Beach</div><div><span class="dot"></span>30 May 2024</div></div>
  <div class="btn-cart">ADD TO CART</div>
</article>
<article class="abs card" style="left:408px">
  <div class="card-img" role="img" aria-label="Timber deck with lounge chairs overlooking forest" style="background:linear-gradient(180deg,#c9ccc6 0%,#5b5a4c 45%,#2e2d29 100%)"></div>
  <span class="badge">NEW</span>
  <h3 class="card-title">FRAMELESS GLASS BALUSTRADE SYSTEMS</h3>
  <div class="card-org">Glass &amp; stainless</div>
  <div class="card-meta"><div><span class="dot"></span>Cannonvale</div><div><span class="dot"></span>30 May 2024</div></div>
  <div class="btn-cart">ADD TO CART</div>
</article>
<article class="abs card" style="left:700px">
  <div class="card-img" role="img" aria-label="Paved pool terrace beside a white modern building" style="background:linear-gradient(180deg,#dfe3e6 0%,#8fa0a8 45%,#5c9ea3 62%,#c7c7c3 100%)"></div>
  <span class="badge">NEW</span>
  <h3 class="card-title">PRIVACY SLAT SCREENS</h3>
  <div class="card-org">Powder coated aluminium</div>
  <div class="card-meta"><div><span class="dot"></span>Bowen</div><div><span class="dot"></span>30 May 2024</div></div>
  <div class="btn-cart">ADD TO CART</div>
</article>
<article class="abs card" style="left:991px">
  <div class="card-img" role="img" aria-label="Sun loungers on a timber deck among palm trees" style="background:linear-gradient(180deg,#9cc0dc 0%,#3f6b35 40%,#d9cfc0 75%,#a0623a 100%)"></div>
  <span class="badge">NEW</span>
  <h3 class="card-title">STAINLESS STEEL HANDRAILS</h3>
  <div class="card-org">Marine grade steel</div>
  <div class="card-meta"><div><span class="dot"></span>Townsville</div><div><span class="dot"></span>30 May 2024</div></div>
  <div class="btn-cart">ADD TO CART</div>
</article>

<h2 class="abs section-title" style="left:0;top:2144px;width:1200px;text-align:center">EXPLORE OUR SERVICES</h2>
<div class="abs map" role="img" aria-label="Grey world map showing service locations">
  <svg class="pin" style="left:60px;top:118px" viewBox="0 0 46 58"><path fill="var(--pin)" d="M23 0a23 23 0 0 1 23 23c0 15-23 35-23 35S0 38 0 23A23 23 0 0 1 23 0z"/><circle cx="23" cy="21" r="10" fill="#fff"/></svg>
  <svg class="pin" style="left:176px;top:290px" viewBox="0 0 46 58"><path fill="var(--pin)" d="M23 0a23 23 0 0 1 23 23c0 15-23 35-23 35S0 38 0 23A23 23 0 0 1 23 0z"/><circle cx="23" cy="21" r="10" fill="#fff"/></svg>
  <svg class="pin" style="left:392px;top:120px" viewBox="0 0 46 58"><path fill="var(--pin)" d="M23 0a23 23 0 0 1 23 23c0 15-23 35-23 35S0 38 0 23A23 23 0 0 1 23 0z"/><circle cx="23" cy="21" r="10" fill="#fff"/></svg>
  <svg class="pin" style="left:593px;top:360px" viewBox="0 0 46 58"><path fill="var(--pin)" d="M23 0a23 23 0 0 1 23 23c0 15-23 35-23 35S0 38 0 23A23 23 0 0 1 23 0z"/><circle cx="23" cy="21" r="10" fill="#fff"/></svg>
</div>

<section class="abs cta" role="img" aria-label="Modern home with lawn and trees at dusk"></section>
<h2 class="abs cta-title">LET'S BRING YOUR VISION TO LIFE</h2>
<p class="abs cta-sub">Whether you're upgrading your home or planning a new build, our experienced team is ready to help create a solution that fits your style and budget.</p>

<footer class="abs footer"></footer>
<div class="abs brand f-brand"><span class="brand-mark"></span><span class="brand-name">Finish Craft Coralbay</span></div>
<p class="abs f-about">Design, fabrication and installation of aluminium, stainless steel and glass for homes and businesses.</p>
<div class="abs f-social"><span></span><span></span><span></span></div>
<div class="abs f-col" style="left:433px"><h4>Quick Links</h4><ul><li>Privacy Screens</li><li>Balustrades</li><li>Glass Fencing</li><li>Pool Fencing</li><li>Gallery</li></ul></div>
<div class="abs f-col" style="left:615px"><h4>Information</h4><ul><li>Handrails</li><li>Electric Gates</li><li>Terms &amp; Conditions</li><li>Privacy Policy</li><li>Sitemap</li></ul></div>
<div class="abs f-col" style="left:819px"><h4>Contact Us</h4><ul>
  <li><span class="ico"></span><b style="font-weight:600">07 4000 5550</b></li>
  <li><span class="ico"></span>hello@finishcraft.example</li>
  <li><span class="ico"></span>Mon – Fri 7am – 7pm &nbsp;&nbsp;&nbsp;&nbsp; Sat 7am – 1pm</li>
  <li><span class="ico"></span>12 Harbour Rd, Cannonvale QLD 4802</li>
</ul></div>
<div class="abs footer-bottom">© 2026 by Finish Craft Coralbay. All Rights Reserved.</div>

</body>
</html>
```